Sheriff Candidate needs a large yard sign

A candidate for Sheriff needs to have a sign to put in front of businesses and houses that advertise her candidacy.

Target Market(s)

Democrats, voters

Industry/Entity Type

Political

Font styles to use
Sans Serif

Colors
34a7d7
3276b5

Requirements
Must have
• Must have her picture
• Must have the words "Elect Dana Whitlock" - I'd like the name Dana to be smaller Whitlock. "Elect" and "Whitlock" should be the focus.
• at the bottom in a box "Paid for by the Committee to Elect Dana Whitlock"
Nice to have
• it would be good to have her logo as well.
• blue color for democrats and on a white background
Should not have
• pink color

```html
<!DOCTYPE html>
<html lang="en">
<head>
<meta charset="UTF-8">
<title>Elect Dana Whitlock – Yard Sign</title>
<link href="https://fonts.googleapis.com/css2?family=Open+Sans:wght@300;400;700;800&display=swap" rel="stylesheet">
<style>
  :root {
    --royal-blue: #3276b5;
    --sky-blue: #34a7d7;
    --white: #ffffff;
    --backdrop: #eef0f2;
    --badge-gold: #caa23c;
    --badge-ink: #3a2c08;
    --photo-top: #d9c2ae;
    --photo-bottom: #1c2433;
  }
  * { margin: 0; padding: 0; box-sizing: border-box; }
  html, body {
    width: 1200px;
    height: 880px;
    overflow: hidden;
    background: var(--backdrop);
    font-family: "Open Sans", Arial, sans-serif;
  }
  .yard-sign {
    position: absolute;
    left: 0;
    top: 79px;
    width: 1200px;
    height: 722px;
    background: var(--white);
    overflow: hidden;
  }
  .sign-shapes {
    position: absolute;
    inset: 0;
  }
  .headline {
    position: absolute;
    left: 78px;
    color: var(--white);
    line-height: 1;
    white-space: nowrap;
  }
  .headline-elect {
    top: 50px;
    font-size: 172px;
    font-weight: 800;
    letter-spacing: 1px;
  }
  .headline-first-name {
    top: 208px;
    font-size: 168px;
    font-weight: 300;
  }
  .headline-last-name {
    top: 368px;
    font-size: 96px;
    font-weight: 800;
    letter-spacing: 1px;
  }
  .disclaimer {
    position: absolute;
    left: 70px;
    top: 560px;
    color: var(--white);
    font-size: 28px;
    font-weight: 400;
    line-height: 46px;
    white-space: nowrap;
  }
  .disclaimer strong { font-weight: 800; }
  .campaign-badge {
    position: absolute;
    left: 550px;
    top: 170px;
    width: 226px;
    height: 226px;
    border-radius: 50%;
    background: var(--badge-gold);
    display: flex;
    align-items: center;
    justify-content: center;
    text-align: center;
    color: var(--badge-ink);
    font-size: 22px;
    font-weight: 700;
    line-height: 1.2;
    text-transform: uppercase;
    padding: 30px;
  }
  .candidate-photo {
    position: absolute;
    left: 790px;
    top: 14px;
    width: 410px;
    height: 708px;
    background: linear-gradient(180deg, var(--photo-top) 0%, var(--photo-top) 28%, var(--photo-bottom) 45%, var(--photo-bottom) 100%);
    border-radius: 160px 160px 0 0;
  }
</style>
</head>
<body>
  <main class="yard-sign">
    <svg class="sign-shapes" width="1200" height="722" viewBox="0 0 1200 722" aria-hidden="true">
      <polygon class="accent-stripe" points="753,0 803,0 595,722 582,722" fill="var(--sky-blue)"/>
      <polygon class="main-panel" points="0,0 753,0 582,722 0,722" fill="var(--royal-blue)"/>
      <polygon class="disclaimer-band" points="0,526 744,526 704,665 0,665" fill="var(--sky-blue)"/>
    </svg>

    <div class="candidate-photo" role="img" aria-label="Portrait photo of candidate Dana Whitlock smiling, wearing a dark blazer"></div>

    <h1 class="headline headline-elect">ELECT</h1>
    <div class="headline headline-first-name">DANA</div>
    <div class="headline headline-last-name">WHITLOCK</div>

    <div class="campaign-badge">Whitlock for Sheriff</div>

    <p class="disclaimer">PAID FOR BY THE<br>COMMITTEE TO <strong>ELECT DANA WHITLOCK</strong></p>
  </main>
</body>
</html>
```